Brochure for new townhouse development

We need a brochure created for our new townhouse development that we can provide to potential purchasers for off-the-plan sales.

2 similar examples are attached.

Brochure content is to include the text as per the attached word document (brochure text) and as follows:
Cover
The Development
At a Glance
The Location - also to include the 2d map and aerial photo (have included screenshot of map and aerial photo as a placeholder, to be replaced in the final version)
Plans - include 3d floor plans, I have included a sample 3d floor plan as a placeholder, this is to be replaced in the final version.
Finishes - as per word document attached, and colour samples attached
Specifications - as per word document attached
Subdivision plan - I have attached a plan which can be used as a placeholder, the final version will be ready next week and is to be replaced in the final version
Landscape plan - as per attached
Rental assessment - as per attached
Stake your Claim

Renders of the building are attached and can be used throughout the brochure.

There is no company name or logo to include.

We have other upcoming developments and would look to reuse the winning brochure so there is future and ongoing work.

```html
<!DOCTYPE html>
<html lang="en">
<head>
<meta charset="utf-8">
<title>At a Glance – Townhouse Development</title>
<link rel="stylesheet" href="https://fonts.googleapis.com/css2?family=Montserrat:wght@400;700&display=swap">
<style>
  :root {
    --page-bg: #ffffff;
    --ink: #2b2426;
    --accent: #0aa0e6;
    --sky-top: #b9d3ec;
    --sky-mid: #dfe6f3;
    --timber: #c9a67a;
    --foliage: #5f7a45;
    --fence: #d9d6d8;
  }
  * { margin: 0; padding: 0; box-sizing: border-box; }
  html, body { width: 1200px; height: 849px; overflow: hidden; background: var(--page-bg); }
  body { font-family: "Montserrat", sans-serif; color: var(--ink); position: relative; }

  .hero-render {
    position: absolute; left: 0; top: 0; width: 1200px; height: 564px;
    background: linear-gradient(180deg, var(--sky-top) 0%, var(--sky-mid) 30%, var(--timber) 62%, var(--foliage) 82%, var(--fence) 100%);
  }

  .section-title {
    position: absolute; left: 337px; top: 589px; width: 248px; height: 48px;
    border: 2px solid var(--accent);
  }
  .section-title svg { position: absolute; left: 0; top: 0; width: 44px; height: 44px; }
  .section-title::after {
    content: ""; position: absolute; left: 44px; top: 0; width: 2px; height: 44px; background: var(--accent);
  }
  .section-title h2 {
    position: absolute; left: 46px; right: 0; top: 0; height: 44px;
    display: flex; align-items: center; justify-content: flex-end; padding-right: 24px;
    font-weight: 700; font-size: 23px; letter-spacing: 0.2px;
  }

  .glance-list {
    position: absolute; left: 630px; top: 590px; width: 384px;
    list-style: none; font-size: 12.4px; line-height: 17.8px; font-weight: 400;
  }
  .glance-list > li { position: relative; padding-left: 23px; margin-bottom: 5px; text-align: justify; }
  .glance-list > li::before {
    content: ""; position: absolute; left: 1px; top: 5px; width: 6px; height: 6px; border-radius: 50%; background: var(--ink);
  }
  .feature-list { list-style: none; margin-top: 0; }
  .feature-list li { position: relative; padding-left: 21px; text-align: justify; }
  .feature-list li::before { content: "o"; position: absolute; left: 0; top: 0; }
</style>
</head>
<body>
  <div class="hero-render" role="img" aria-label="Architectural render of timber-clad gabled townhouses behind rendered front walls, with trees and evening sky"></div>

  <div class="section-title">
    <svg viewBox="0 0 44 44" aria-hidden="true"><polygon points="44,0 44,44 0,44" fill="var(--accent)"/></svg>
    <h2>At a Glance</h2>
  </div>

  <ul class="glance-list">
    <li>Two blocks of three architecturally designed townhouses</li>
    <li>Each townhouse includes:
      <ul class="feature-list">
        <li>Open-plan living, dining and high-spec kitchen</li>
        <li>Seamless flow to easy-care courtyard garden</li>
        <li>Two double bedrooms, all with built-in wardrobes (two townhouses with WIR in master)</li>
        <li>Two en suite tiled bathrooms</li>
        <li>Single internal-access garage with laundry</li>
      </ul>
    </li>
    <li>Smart design, high-quality fixtures and fittings, and freehold titles</li>
  </ul>
</body>
</html>
```